I need this done FAST!
Business Cards and Stationary for new home construction company - Construction
Simple
Gerald Finch
Owner
4816 Marlow Ct #306142 Houston, TX 77391
Gerald@thequillstoneframeworks.com
www.thequillstoneframeworks.com
I would like this business card to be minimal in its design. I just want it to be a way of saying ... Hi, call me directly. It does not need to be an advertisement. I need the vector files of this please
Front should be the logo only, and the back should be this information: Design~Build Firm Gerald Finch, Owner Phone Email Web address

```html
<!DOCTYPE html>
<html lang="en">
<head>
<meta charset="utf-8">
<title>Quillstone Frameworks – Business Cards</title>
<link href="https://fonts.googleapis.com/css2?family=Montserrat:wght@400;600;700&family=Open+Sans:wght@400;600&display=swap" rel="stylesheet">
<style>
  :root {
    --red: #c8141c;
    --red-dark: #8e0c12;
    --grey: #b9b9bb;
    --grey-light: #e4e4e6;
    --ink: #2b2b2d;
    --paper: #ffffff;
    --backdrop: #3a3a3c;
  }
  * { box-sizing: border-box; margin: 0; padding: 0; }
  html, body { width: 1200px; height: 782px; overflow: hidden; }
  body {
    background: var(--backdrop);
    font-family: "Open Sans", Arial, sans-serif;
    position: relative;
  }
  .card {
    position: absolute;
    top: 236px;
    width: 530px;
    height: 310px;
    background: var(--paper);
    border-radius: 22px;
    overflow: hidden;
  }
  .card--front { left: 50px; }
  .card--back { left: 620px; }
  .card__swoosh { position: absolute; inset: 0; width: 100%; height: 100%; }

  .brand {
    position: absolute;
    display: flex;
    flex-direction: column;
    align-items: center;
  }
  .brand__row { display: flex; align-items: center; gap: 10px; }
  .brand__mark { width: 22px; height: 22px; background: var(--red); flex: none; }
  .brand__name {
    font-family: "Montserrat", Arial, sans-serif;
    font-weight: 700;
    color: var(--red);
    text-transform: uppercase;
    letter-spacing: 0.5px;
    line-height: 1.05;
    text-align: center;
  }
  .brand__tagline {
    margin-top: 6px;
    font-family: "Montserrat", Arial, sans-serif;
    font-size: 8px;
    letter-spacing: 3px;
    color: var(--grey);
    text-transform: uppercase;
  }
  .card--front .brand { left: 0; right: 0; top: 128px; }
  .card--front .brand__name { font-size: 26px; }
  .card--back .brand { left: 30px; top: 150px; width: 230px; }
  .card--back .brand__name { font-size: 20px; }

  .holder {
    position: absolute;
    right: 30px;
    top: 46px;
    text-align: right;
    color: var(--paper);
    font-family: "Montserrat", Arial, sans-serif;
  }
  .holder__name { font-size: 17px; font-weight: 600; }
  .holder__title { font-size: 13px; font-weight: 400; margin-top: 2px; }

  .contact {
    position: absolute;
    left: 280px;
    top: 132px;
    width: 236px;
    padding-left: 14px;
    border-left: 2px solid var(--red);
    color: var(--ink);
    font-size: 11.5px;
    line-height: 1.5;
    list-style: none;
  }
  .contact__item { display: flex; align-items: flex-start; gap: 6px; margin-bottom: 4px; white-space: nowrap; }
  .contact__icon { width: 11px; height: 11px; flex: none; margin-top: 3px; fill: var(--red); }
  .contact__item--web { padding-left: 17px; }
</style>
</head>
<body>

  <section class="card card--front" aria-label="Business card front">
    <svg class="card__swoosh" viewBox="0 0 530 310" preserveAspectRatio="none" aria-hidden="true">
      <path d="M0 0 H530 V118 C430 60 250 38 0 58 Z" fill="var(--grey-light)"/>
      <path d="M0 0 H530 V100 C430 46 250 26 0 42 Z" fill="var(--grey)"/>
      <path d="M0 0 H530 V86 C420 30 240 16 0 30 Z" fill="var(--red)"/>
      <path d="M0 0 H530 V40 C400 8 220 4 0 10 Z" fill="var(--red-dark)" opacity="0.35"/>
    </svg>
    <div class="brand">
      <div class="brand__row">
        <span class="brand__mark"></span>
        <span class="brand__name">Quillstone<br>Frameworks</span>
      </div>
      <span class="brand__tagline">Design Build Firm</span>
    </div>
  </section>

  <section class="card card--back" aria-label="Business card back">
    <svg class="card__swoosh" viewBox="0 0 530 310" preserveAspectRatio="none" aria-hidden="true">
      <path d="M120 0 H530 V128 C470 110 390 100 300 96 C230 92 170 60 120 0 Z" fill="var(--grey-light)"/>
      <path d="M150 0 H530 V116 C470 96 390 88 310 84 C240 80 190 50 150 0 Z" fill="var(--red)"/>
      <path d="M250 0 H530 V50 C450 36 330 30 250 0 Z" fill="var(--red-dark)" opacity="0.3"/>
    </svg>
    <div class="holder">
      <p class="holder__name">Gerald Finch</p>
      <p class="holder__title">Owner</p>
    </div>
    <div class="brand">
      <div class="brand__row">
        <span class="brand__mark"></span>
        <span class="brand__name">Quillstone<br>Frameworks</span>
      </div>
      <span class="brand__tagline">Design Build Firm</span>
    </div>
    <ul class="contact">
      <li class="contact__item">
        <svg class="contact__icon" viewBox="0 0 12 12" aria-hidden="true"><path d="M6 0a4 4 0 0 1 4 4c0 3-4 8-4 8S2 7 2 4a4 4 0 0 1 4-4zm0 2.5a1.5 1.5 0 1 0 0 3 1.5 1.5 0 0 0 0-3z"/></svg>
        <span>4816 Marlow Ct #306142<br>Houston, TX 77391</span>
      </li>
      <li class="contact__item">
        <svg class="contact__icon" viewBox="0 0 12 12" aria-hidden="true"><path d="M2.5 0.5l2 2.5-1.2 1.4c.8 1.7 2 2.9 3.6 3.7L8.3 7l2.7 2-1.2 2.5C5 11.3.7 7 .5 2z"/></svg>
        <span>713 555 0148</span>
      </li>
      <li class="contact__item">
        <svg class="contact__icon" viewBox="0 0 12 12" aria-hidden="true"><path d="M0 2h12v1.2L6 7 0 3.2zM0 4.6l6 3.8 6-3.8V10H0z"/></svg>
        <span>Gerald@thequillstoneframeworks.com</span>
      </li>
      <li class="contact__item contact__item--web">
        <span>www.thequillstoneframeworks.com</span>
      </li>
    </ul>
  </section>

</body>
</html>
```